Sales Process

I need a card/page to hand out to my new clients that gives them an over view of our sales process start to finish. Along with 3 points that set us apart from all other competition.
The attached file is my first attempt with other ideas so give your suggestions.
Check out my website to get an idea of who we are. www.brightmeadowyards.com

```html
<!DOCTYPE html>
<html lang="en">
<head>
<meta charset="utf-8">
<title>Bright Meadow Yards – Our Process</title>
<link rel="stylesheet" href="https://fonts.googleapis.com/css2?family=Cinzel:wght@700&family=Poppins:wght@400;500;600&display=swap">
<style>
  :root {
    --backdrop: #f0f0f1;
    --card: #ffffff;
    --green: #7dc242;
    --ink: #4a4a4a;
    --ink-soft: #5b5b5b;
    --sun: #fde2c0;
    --white: #ffffff;
  }
  * { margin: 0; padding: 0; box-sizing: border-box; }
  html, body { width: 1200px; height: 804px; overflow: hidden; background: var(--backdrop); }
  body { position: relative; font-family: "Poppins", Arial, sans-serif; color: var(--ink-soft); }

  .card { position: absolute; left: 83px; top: 29px; width: 1028px; height: 728px; background: var(--card); }

  .process-art { position: absolute; left: 0; top: 0; width: 1200px; height: 804px; }

  .brand { position: absolute; left: 140px; top: 92px; display: flex; flex-direction: column; align-items: flex-start; }
  .brand-row { display: flex; align-items: center; gap: 7px; }
  .brand-dot { width: 14px; height: 14px; border-radius: 50%; background: var(--green); }
  .brand-name { font-weight: 600; font-size: 17px; color: var(--green); line-height: 1.1; }
  .brand-tagline { font-size: 6.5px; color: var(--ink); margin-top: 6px; letter-spacing: 0.3px; }

  .value-title { position: absolute; left: 140px; top: 186px; font-family: "Cinzel", Georgia, serif; font-weight: 700; font-size: 22px; color: var(--ink); letter-spacing: 0.3px; }
  .value-title .accent { color: var(--green); }

  .value-list { position: absolute; left: 140px; top: 224px; list-style: none; }
  .value-list li { display: flex; align-items: center; gap: 10px; font-size: 11.5px; height: 25.5px; color: var(--ink-soft); }
  .value-list .bullet { width: 11px; height: 13px; background: var(--green); border-radius: 0 80% 0 80%; transform: rotate(10deg); }

  .apart-band { position: absolute; left: 83px; top: 303px; width: 350px; height: 48px; background: var(--green); color: var(--white); font-size: 14.5px; letter-spacing: 2.6px; display: flex; align-items: center; justify-content: center; }

  .step { position: absolute; transform: translateX(-50%); text-align: center; font-size: 12.5px; line-height: 1.3; color: var(--ink-soft); white-space: nowrap; }
  .step-call { left: 371px; top: 628px; }
  .step-visit { left: 442px; top: 481px; }
  .step-design { left: 599px; top: 446px; }
  .step-install { left: 680px; top: 298px; }
  .step-complete { left: 838px; top: 215px; font-size: 13px; line-height: 1.27; color: var(--ink); }
</style>
</head>
<body>
  <div class="card"></div>

  <svg class="process-art" viewBox="0 0 1200 804">
    <circle class="finish-disc" cx="834" cy="240" r="82" fill="var(--sun)"/>

    <path class="process-line" fill="none" stroke="var(--green)" stroke-width="4" stroke-linecap="round"
      d="M287,653 C320,710 430,700 440,635 C448,585 400,565 380,535 C350,490 365,410 415,398 C470,385 520,420 535,460 C555,505 620,520 660,490 C695,462 690,420 665,385 C630,335 615,270 640,220 C665,175 720,180 740,225 C744,234 747,240 750,244"/>

    <g class="step-icons" fill="none" stroke="var(--ink)" stroke-width="1.4" stroke-linecap="round" stroke-linejoin="round">
      <g class="icon-call">
        <path d="M347,590 c-4,4 -3,12 5,20 c8,8 16,9 20,5 l-5,-7 l-5,3 c-4,-3 -8,-7 -11,-11 l3,-5 z"/>
        <rect x="372" y="576" width="14" height="10" rx="1.5"/>
      </g>
      <g class="icon-house">
        <path d="M424,470 V455 L444,441 L464,455 V470"/>
        <path d="M418,459 L444,438 L470,459"/>
        <rect x="440" y="459" width="9" height="11"/>
        <path d="M474,470 V457"/>
        <ellipse cx="474" cy="450" rx="4" ry="7"/>
        <path d="M414,471 H484"/>
      </g>
      <g class="icon-design">
        <path d="M576,437 V424 M584,437 V424 M592,437 V424 M600,437 V424 M572,428 H604"/>
        <path d="M609,437 V421"/>
        <ellipse cx="609" cy="413" rx="5" ry="8"/>
        <path d="M578,410 c0,-5 8,-6 9,-1 c4,-2 7,1 5,4 H578"/>
        <path d="M570,438 H620"/>
      </g>
      <g class="icon-install">
        <rect x="672" y="262" width="28" height="18" rx="2"/>
        <path d="M672,270 H700"/>
        <path d="M680,262 V256 H692 V262"/>
        <rect x="683" y="268" width="6" height="5"/>
      </g>
      <g class="icon-complete">
        <rect x="824" y="170" width="24" height="32" rx="1.5"/>
        <circle cx="836" cy="181" r="6"/>
        <path d="M833,181 l2.5,2.5 l3.5,-5"/>
        <path d="M829,193 H843 M829,197 H839"/>
      </g>
    </g>
  </svg>

  <div class="brand">
    <div class="brand-row">
      <span class="brand-dot"></span>
      <span class="brand-name">Bright Meadow Yards</span>
    </div>
    <span class="brand-tagline">Lawn Design And Garden Care</span>
  </div>

  <h1 class="value-title">List Our <span class="accent">Value To You</span></h1>

  <ul class="value-list">
    <li><span class="bullet"></span>Lorem ipsum dolor sit amet, consectetuer</li>
    <li><span class="bullet"></span>Lorem ipsum dolor sit amet, consectetuer</li>
    <li><span class="bullet"></span>Lorem ipsum dolor sit amet, consectetuer</li>
  </ul>

  <div class="apart-band">3 Things That Set Us Apart</div>

  <p class="step step-call">Initial Call<br>Can We Help?</p>
  <p class="step step-visit">Site Visit,<br>Discuss, Plan,<br>Dream</p>
  <p class="step step-design">Design<br>Proposed</p>
  <p class="step step-install">Installation<br>Construction</p>
  <p class="step step-complete">Complete<br>Kick Back+<br>Relax With A<br>Smile On Your<br>Face</p>
</body>
</html>
```